A comunicação apenas pelo chat ou com desenvolvedor que não se comunica com cliente é péssimo ! O desenvolvedor que não se comunica dificulta o desenvolvimento do trabalho causando uma demora ecessiva !

```html
<!DOCTYPE html>
<html lang="pt-BR">
<head>
<meta charset="utf-8">
<title>Traço Norte – Cartão de visita</title>
<link rel="stylesheet" href="https://fonts.googleapis.com/css2?family=Roboto:wght@400;500&display=swap">
<style>
  :root {
    --page: #ffffff;
    --frame: #d4d4d4;
    --card: #000000;
    --brand-grey: #c4c4c4;
    --band: #363636;
    --band-dark: #2a2a2a;
    --text-light: #ffffff;
    --text-muted: #9a9a9a;
  }
  * { margin: 0; padding: 0; box-sizing: border-box; }
  html, body { width: 1200px; height: 1200px; overflow: hidden; background: var(--page); }
  .sheet {
    position: relative; width: 1200px; height: 1200px;
    font-family: "Roboto", Arial, sans-serif;
  }
  .sheet-frame {
    position: absolute; left: 14px; top: 14px; right: 14px; bottom: 14px;
    border: 2px solid var(--frame);
  }
  .card {
    position: absolute; left: 209px; width: 782px;
    background: var(--card); overflow: hidden;
  }
  .card-front { top: 91px; height: 449px; }
  .card-back { top: 655px; height: 454px; }

  /* front */
  .brand {
    position: absolute; left: 0; right: 0; top: 0; bottom: 0;
    display: flex; align-items: center; justify-content: center; gap: 18px;
  }
  .brand-mark { width: 30px; height: 30px; background: var(--brand-grey); }
  .brand-name {
    font-family: "Roboto", Arial, sans-serif; font-weight: 500;
    font-size: 52px; letter-spacing: 2px; line-height: 1;
    color: var(--brand-grey);
  }

  /* back */
  .back-band {
    position: absolute; left: 0; top: 161px; width: 491px; height: 293px;
    background: linear-gradient(90deg, var(--band) 0%, var(--band-dark) 100%);
  }
  .back-brand {
    position: absolute; left: 91px; top: 206px;
    font-family: "Roboto", Arial, sans-serif; font-weight: 500;
    font-size: 40px; letter-spacing: 2px; line-height: 1;
    color: var(--brand-grey);
  }
  .holder { position: absolute; right: 50px; top: 100px; text-align: right; }
  .holder-name { font-size: 30px; font-weight: 500; color: var(--text-light); line-height: 1.1; }
  .holder-role { font-size: 21px; color: var(--text-muted); }
  .contacts {
    position: absolute; right: 50px; top: 200px; list-style: none;
    color: var(--text-light); font-size: 18px;
  }
  .contact-item {
    display: flex; align-items: center; justify-content: flex-end; gap: 10px;
    height: 29px; white-space: nowrap;
  }
  .contact-item.gap-before { margin-top: 17px; }
  .contact-icon { width: 20px; height: 20px; flex: none; }
</style>
</head>
<body>
<main class="sheet">
  <div class="sheet-frame"></div>

  <section class="card card-front">
    <div class="brand">
      <span class="brand-mark"></span>
      <span class="brand-name">TRAÇO NORTE</span>
    </div>
  </section>

  <section class="card card-back">
    <div class="back-band" role="img" aria-label="Faixa decorativa em cinza escuro"></div>
    <div class="back-brand">TRAÇO NORTE</div>

    <div class="holder">
      <p class="holder-name">Nome Sobrenome</p>
      <p class="holder-role">cargo</p>
    </div>

    <ul class="contacts">
      <li class="contact-item">+55 31 4000-1234
        <svg class="contact-icon" viewBox="0 0 20 20"><circle cx="10" cy="10" r="8.5" fill="none" stroke="#fff" stroke-width="1.6"/><path d="M7 5.5l2 2-1 1.3c.6 1.3 1.5 2.2 2.8 2.8l1.3-1 2 2-1.2 1.4c-3.5-.4-6.3-3.2-6.7-6.7z" fill="#fff"/></svg>
      </li>
      <li class="contact-item">contato@traconorte.com.br
        <svg class="contact-icon" viewBox="0 0 20 20"><rect x="2" y="5" width="16" height="11" fill="#fff"/><path d="M2 5l8 6 8-6" fill="none" stroke="#000" stroke-width="1.4"/></svg>
      </li>
      <li class="contact-item">www.traconorte.com.br
        <svg class="contact-icon" viewBox="0 0 20 20"><g fill="none" stroke="#fff" stroke-width="1.5"><circle cx="10" cy="10" r="8"/><ellipse cx="10" cy="10" rx="3.5" ry="8"/><path d="M2 10h16M3.5 6h13M3.5 14h13"/></g></svg>
      </li>
      <li class="contact-item gap-before">Endereço: Rua Alfa - N 42
        <svg class="contact-icon" viewBox="0 0 20 20"><circle cx="10" cy="10" r="6.5" fill="none" stroke="#fff" stroke-width="2.4"/></svg>
      </li>
      <li class="contact-item">/traconorte
        <svg class="contact-icon" viewBox="0 0 20 20"><rect x="2.5" y="2.5" width="15" height="15" rx="2" fill="#fff"/></svg>
      </li>
    </ul>
  </section>
</main>
</body>
</html>
```